Brightbay Business Card Design

Our company is called Brightbay. We manufacture confectionary snacks & frozen novelties. Our initial product portfolio includes frozen ice lollies/popsicles & stick ice cream bars.

We require a business card design.

Please use the attached Logo.

Please use an orange, brown, yellow colour code. You may choose any combination of the 3 or include all three. The logo however must remain orange.

Target Market(s)

Business card will be targeted at distributors of our products such as supermarket procurement managers, convenience store owners, wholesale distributors and merchandising agents.

Industry/Entity Type

Business

Requirements
Must have
• Calvin Obeng_Director/ P.O.Box Dunmore 5172, Accra, Ghana / m: 00233(0)507318924/ e: calvin.obeng@mailvora.co.uk

```html
<!DOCTYPE html>
<html lang="en">
<head>
<meta charset="utf-8">
<title>Brightbay Business Card</title>
<link rel="stylesheet" href="https://fonts.googleapis.com/css2?family=Tinos:wght@400;700&family=Archivo+Black&display=swap">
<style>
  :root {
    --card-orange: #f8a51b;
    --ring-orange: #f7941d;
    --sun-yellow: #ffe100;
    --cocoa-brown: #3c2a1b;
    --ink-brown: #2a1a0d;
    --brand-orange: #e2541c;
  }
  html, body {
    margin: 0;
    padding: 0;
    overflow: hidden;
    background: #ffffff;
  }
  .business-card {
    position: relative;
    width: 1200px;
    height: 699px;
    overflow: hidden;
    background: var(--card-orange);
  }
  .top-band {
    position: absolute;
    left: 0;
    top: 0;
    width: 1200px;
    height: 190px;
    background: var(--cocoa-brown);
  }
  .decor-area {
    position: absolute;
    left: 580px;
    top: 0;
    width: 620px;
    height: 600px;
    border-bottom-left-radius: 300px;
    background: radial-gradient(circle at 480px 300px, var(--sun-yellow) 0%, #fcc313 45%, var(--ring-orange) 100%);
  }
  .brand-lockup {
    position: absolute;
    left: 96px;
    top: 300px;
    display: flex;
    align-items: center;
    gap: 18px;
  }
  .brand-dot {
    width: 58px;
    height: 58px;
    border-radius: 50%;
    background: var(--brand-orange);
  }
  .brand-name {
    font-family: "Tinos", serif;
    font-weight: 700;
    font-size: 86px;
    line-height: 1;
    color: var(--brand-orange);
    letter-spacing: -1px;
  }
  .contact-block {
    position: absolute;
    left: 45px;
    top: 458px;
    color: var(--ink-brown);
  }
  .contact-name {
    font-family: "Archivo Black", sans-serif;
    font-style: italic;
    font-size: 36px;
    line-height: 1;
    margin: 0 0 12px 0;
  }
  .contact-line {
    font-family: "Tinos", serif;
    font-size: 42px;
    line-height: 50px;
    margin: 0;
  }
</style>
</head>
<body>
<div class="business-card">
  <div class="top-band"></div>
  <div class="decor-area" role="img" aria-label="Decorative pattern of concentric yellow and orange rings with flowing wave bands"></div>

  <div class="brand-lockup">
    <span class="brand-dot"></span>
    <span class="brand-name">Brightbay</span>
  </div>

  <div class="contact-block">
    <p class="contact-name">Calvin Obeng - Director</p>
    <p class="contact-line">P.O.Box Dunmore 5172, Accra, Ghana</p>
    <p class="contact-line">m: 00233(0)507318924</p>
    <p class="contact-line">e: calvin.obeng@mailvora.co.uk</p>
  </div>
</div>
</body>
</html>
```